Soap box for artisan soaps, eco-look, high design

We need a soap box for our lovely artisan soaps. The box size is: 9 cm height x 6,5 cm width x 2,8 cm depth. It would be nice when there is a small window in the box so you can see the soap.

See attachment for an example soap box (upside down). Please use the same elements such as texts and industrie logos. The idea is that we have a generic design that we can custom-made for different soaps. We have 15 different soaps in total at the moment.

Target Market(s)

Middle to high income

Font styles to use
Decorative
Script

Requirements
Must have
• Dutch text:
• Etherische oliën
• Handgemaakt
• Natuurlijke ingrediënten

```html
<!DOCTYPE html>
<html lang="nl">
<head>
<meta charset="utf-8">
<title>Velmora – Lemon and Poppy soap box dieline</title>
<link href="https://fonts.googleapis.com/css2?family=Arimo:wght@400;700&family=Allura&display=swap" rel="stylesheet">
<style>
  :root {
    --kraft: #bd9a77;
    --kraft-dotted: #b39171;
    --ink: #1c1a18;
    --navy: #17466b;
    --white: #ffffff;
    --lemon: #d8bf4c;
    --fold: #e0462f;
    --cut: #1c1a18;
  }
  html, body {
    margin: 0;
    padding: 0;
    width: 1200px;
    height: 1200px;
    overflow: hidden;
    background: var(--white);
  }
  .dieline { display: block; width: 1200px; height: 1200px; }
  .sheet { fill: var(--kraft); }
  .pattern-area { fill: var(--kraft-dotted); }
  .lemon-band { fill: var(--lemon); }
  .cut-line { fill: none; stroke: var(--cut); stroke-width: 1.2; }
  .fold-line { fill: none; stroke: var(--fold); stroke-width: 1; }
  .window { fill: #000; }
  .body-text { font-family: "Arimo", Arial, sans-serif; fill: var(--ink); }
  .brand-name { font-family: "Arimo", Arial, sans-serif; font-weight: 700; fill: var(--navy); }
  .script { font-family: "Allura", cursive; fill: var(--ink); }
  .product-type { font-family: "Arimo", Arial, sans-serif; font-size: 21px; fill: var(--ink); letter-spacing: 0.5px; }
  .claims { font-family: "Arimo", Arial, sans-serif; font-size: 21px; fill: var(--white); }
  .side-copy { font-size: 11px; }
  .back-title { font-size: 16px; }
  .back-copy { font-size: 12.4px; }
  .free-from { font-size: 10.5px; }
  .free-from-box { fill: none; stroke: var(--ink); stroke-width: 0.8; }
  .weight { font-family: "Arimo", Arial, sans-serif; font-size: 27px; fill: var(--ink); }
  .badge { fill: var(--ink); }
  .badge-outline { fill: none; stroke: var(--ink); stroke-width: 1; }
  .maker { fill: var(--white); font-size: 42px; }
  .address { font-family: "Arimo", Arial, sans-serif; font-size: 18px; fill: var(--white); }
</style>
</head>
<body>
<svg class="dieline" viewBox="0 0 1390 1390" xmlns="http://www.w3.org/2000/svg">
  <!-- kraft sheet -->
  <rect class="sheet" x="124" y="190" width="1144" height="1036"/>

  <!-- dotted lower zone and lemon band -->
  <rect class="pattern-area" x="143" y="735" width="1044" height="225" role="img" aria-label="Fine dark dot pattern across the lower part of the box"/>
  <rect class="lemon-band" x="143" y="722" width="1044" height="13"/>

  <!-- cut lines: flaps -->
  <g class="cut-line">
    <polyline points="143,456 143,960"/>
    <polyline points="160,456 160,310 260,310 298,456"/>
    <polyline points="150,960 160,1107 260,1107 298,960"/>
    <polyline points="665,456 703,310 797,310 805,456"/>
    <polyline points="665,960 703,1107 797,1107 805,960"/>
    <path d="M820,456 V295 H853 V320 M820,295 C820,250 845,225 880,208 H1130 C1165,225 1187,250 1187,295 V456 M1187,295 H1155 V320"/>
    <path d="M820,960 V1120 H853 V1095 M820,1120 C820,1165 845,1190 880,1208 H1130 C1165,1190 1187,1165 1187,1120 V960 M1187,1120 H1155 V1095"/>
    <polyline points="1187,456 1250,470 1250,945 1187,960"/>
  </g>

  <!-- fold lines -->
  <g class="fold-line">
    <line x1="143" y1="456" x2="1187" y2="456"/>
    <line x1="143" y1="960" x2="1187" y2="960"/>
    <line x1="298" y1="456" x2="298" y2="960"/>
    <line x1="665" y1="456" x2="665" y2="960"/>
    <line x1="820" y1="456" x2="820" y2="960"/>
    <line x1="1187" y1="456" x2="1187" y2="960"/>
    <line x1="853" y1="298" x2="1155" y2="298"/>
    <line x1="853" y1="1118" x2="1155" y2="1118"/>
  </g>

  <!-- front panel -->
  <g class="front-panel" text-anchor="middle">
    <text class="brand-name" x="481" y="522" font-size="46">Velmora</text>
    <text class="script" x="481" y="580" font-size="46">Lemon and Poppy</text>
    <text class="product-type" x="481" y="616">ETHERISCHE ZEEP</text>
    <circle class="window" cx="483" cy="729" r="95"/>
    <text class="claims" x="483" y="873">Etherische oliën</text>
    <text class="claims" x="483" y="905">Handgemaakt</text>
    <text class="claims" x="479" y="937">Natuurlijke ingrediënten</text>
  </g>

  <!-- left side: ingredients -->
  <g class="body-text side-copy" transform="translate(160,715) rotate(-90)">
    <text x="0" y="0"><tspan font-weight="700" font-style="italic">Ingredients:</tspan> Olijf olie pomace (Olea europaea),</text>
    <text x="0" y="13.5">Kokosnoot olie (Cocos nucifera), Palm olie</text>
    <text x="0" y="27">(Elaeis Guineensis Kernel Oil), Water (Aqua),</text>
    <text x="0" y="40.5">Citroen Etherische Olie (Citrus limonum), maan-</text>
    <text x="0" y="54">zaad (Papaver somniferum), ijzer oxide geel (Iron</text>
    <text x="0" y="67.5">Oxide). Natuurlijke bestanddelen van Etherische</text>
    <text x="0" y="81">Olie – Citral, Citronellol, Geraniol,</text>
    <text x="0" y="94.5">Limonene, Linalool.</text>
  </g>

  <!-- spine: product story -->
  <g class="body-text side-copy" transform="translate(805,463) rotate(90)">
    <text x="0" y="0">Essentiële oliën van Lemon creëren een leven-</text>
    <text x="0" y="13.5">dige explosie van positieve goodness, waardoor</text>
    <text x="0" y="27">u vrolijk wakker wordt. Poppy seeds worden</text>
    <text x="0" y="40.5">toegevoegd om een beetje kracht te geven bij</text>
    <text x="0" y="54">het exfoliëren. "Lemon helpt je in een positieve</text>
    <text x="0" y="67.5">state of mind te komen, waardoor je de dag</text>
    <text x="0" y="81">beter aan kan.</text>
  </g>

  <!-- back panel -->
  <g class="back-panel">
    <text class="body-text back-title" x="838" y="479">Onze zeep</text>
    <g class="body-text back-copy">
      <text x="838" y="503">Het geeft jouw huid een heerlijk gevoel met zachte bub-</text>
      <text x="838" y="520">bels en rijke geur! Handgemaakt in kleine batches met</text>
      <text x="838" y="537">eerlijke ingrediënten en essentiële oliën. Elke zeep wordt</text>
      <text x="838" y="554">alleen geproduceerd als het iets goeds voor je doet en</text>
      <text x="838" y="571">droogt minstens zes weken voordat ze worden verpakt.</text>
      <text x="838" y="588">Ze zien er te mooi uit om te openen, maar hoe ga je dan</text>
      <text x="838" y="605">genieten van de heerlijke bubbels, de ongelooflijke geur</text>
      <text x="838" y="622">en je zachte, zijdeachtige huid?</text>
    </g>

    <rect class="free-from-box" x="835" y="638" width="192" height="77"/>
    <g class="body-text free-from">
      <text x="846" y="651">Vrij van:</text>
      <text x="840" y="666">• SLA &amp; SLSA</text>
      <text x="840" y="680">• Alcohol &amp; Parabenen</text>
      <text x="840" y="695">• Sorbaten &amp; Siliconen</text>
      <text x="840" y="709">• Sulfaat &amp; Conserveringsmiddelen</text>
    </g>

    <text class="weight" x="1037" y="661">120g ℮</text>
    <circle class="badge" cx="1055" cy="695" r="13" role="img" aria-label="Recycling badge"/>
    <g role="img" aria-label="Packaging disposal badge">
      <ellipse class="badge-outline" cx="1094" cy="688" rx="12" ry="5"/>
      <path class="badge-outline" d="M1082,688 V703 A12,5 0 0 0 1106,703 V688"/>
    </g>

    <text class="script maker" x="1045" y="800" text-anchor="middle">Lotte Brandsma</text>
    <text class="brand-name" x="1035" y="885" font-size="44" text-anchor="middle">Velmora</text>
    <text class="address" x="963" y="919">Oudewater, Nederland</text>
    <text class="address" x="963" y="943">velmora.nl</text>
  </g>
</svg>
</body>
</html>
```